Veltrano - Mechanic/Collision Center Business Card

We're looking for a business card design for our mechanic/ collision repair shop.

Can be with colours or monochromatic.

See the attached files.

Many thanks

```html
<!DOCTYPE html>
<html lang="pt">
<head>
<meta charset="utf-8">
<title>Veltrano – Business Card</title>
<link href="https://fonts.googleapis.com/css2?family=Michroma&family=Arimo:wght@400;500&display=swap" rel="stylesheet">
<style>
  :root {
    --page: #ffffff;
    --ink: #000000;
    --steel-dark: #2b2b2d;
    --steel-mid: #3d3d40;
    --steel-light: #4a4a4e;
    --brand-blue: #2e779e;
    --band: #ffffff;
    --link: #2e779e;
    --text-light: #ffffff;
  }
  * { margin: 0; padding: 0; box-sizing: border-box; }
  html, body {
    width: 1200px; height: 1200px; overflow: hidden;
    background: var(--page);
    font-family: "Arimo", Arial, sans-serif;
  }
  .sheet { position: relative; width: 1200px; height: 1200px; }
  .view-label {
    position: absolute; left: 0; width: 1200px; text-align: center;
    font-size: 53px; line-height: 62px; font-weight: 400; color: var(--ink);
    font-family: "Arimo", Arial, sans-serif;
  }
  .view-label--front { top: 12px; }
  .view-label--back { top: 616px; }

  .card {
    position: absolute; left: 270px; width: 660px; height: 428px;
    border-radius: 16px; overflow: hidden;
    background: var(--brand-blue);
    color: var(--text-light);
  }
  .card--front { top: 86px; }
  .card--back { top: 686px; }

  .metal-panel {
    position: absolute; left: 0; top: 0; width: 330px; height: 100%;
    background: radial-gradient(ellipse at 60% 40%, var(--steel-light) 0%, var(--steel-mid) 45%, var(--steel-dark) 100%);
  }

  .wordmark {
    position: absolute; font-family: "Michroma", sans-serif;
    color: var(--text-light); white-space: nowrap; text-align: center;
  }
  .card--front .wordmark { left: 110px; top: 138px; width: 440px; font-size: 44px; line-height: 52px; }
  .card--back .wordmark { left: 356px; top: 136px; width: 276px; font-size: 31px; line-height: 38px; }

  .person-name {
    position: absolute; font-family: "Michroma", sans-serif;
    letter-spacing: 2px; white-space: nowrap;
  }
  .person-role { position: absolute; white-space: nowrap; }
  .card--front .person-name { left: 67px; top: 262px; font-size: 24px; line-height: 30px; }
  .card--front .person-role { left: 67px; top: 296px; font-size: 14px; line-height: 17px; }
  .card--back .person-name { left: 360px; top: 259px; font-size: 25px; line-height: 30px; }
  .card--back .person-role { left: 360px; top: 296px; font-size: 15px; line-height: 19px; }

  .contact-list { position: absolute; left: 0; top: 0; list-style: none; }
  .contact-item {
    position: absolute; left: 374px; display: flex; align-items: flex-start; gap: 6px;
    font-size: 14px; line-height: 18px; white-space: nowrap;
  }
  .contact-item svg { width: 16px; height: 16px; flex: none; margin-top: 1px; }
  .contact-item--address { top: 266px; }
  .contact-item--phone { top: 328px; }
  .contact-item--email { top: 353px; }
  .contact-item--web { top: 379px; }
  .contact-text { padding-left: 3px; }

  .stripe-top {
    position: absolute; left: 0; top: 19px; width: 660px; height: 15px;
  }
  .stripe-bottom {
    position: absolute; left: 0; top: 391px; width: 660px; height: 17px;
    background: var(--band); text-align: center;
    font-size: 12px; line-height: 17px; color: var(--link);
  }
  .services-title {
    position: absolute; left: 32px; top: 144px;
    font-family: "Michroma", sans-serif; font-size: 23px; line-height: 28px;
    letter-spacing: 2px; font-weight: 400; white-space: nowrap;
  }
  .services-list { position: absolute; left: 32px; top: 189px; list-style: none; }
  .service {
    display: flex; align-items: center; gap: 8px;
    font-size: 23px; line-height: 31px; white-space: nowrap;
  }
  .service::before {
    content: ""; width: 17px; height: 17px; border-radius: 50%;
    background: var(--text-light); flex: none;
  }
</style>
</head>
<body>
<div class="sheet">
  <h1 class="view-label view-label--front">Front View</h1>

  <section class="card card--front">
    <div class="metal-panel" role="img" aria-label="Dark perforated metal texture background"></div>
    <div class="wordmark">VELTRANO</div>

    <div class="person-name">RUI MATOS</div>
    <div class="person-role">Managing Director<br>+351 910482736</div>

    <ul class="contact-list">
      <li class="contact-item contact-item--address">
        <svg viewBox="0 0 16 16" aria-hidden="true"><path d="M8 1a5 5 0 0 0-5 5c0 3.6 5 9 5 9s5-5.4 5-9a5 5 0 0 0-5-5zm0 7a2 2 0 1 1 0-4 2 2 0 0 1 0 4z" fill="none" stroke="#fff" stroke-width="1.6"/></svg>
        <span class="contact-text">Rua das Oficinas, 42<br>Postal code | 1900-318<br>Lisboa</span>
      </li>
      <li class="contact-item contact-item--phone">
        <svg viewBox="0 0 16 16" aria-hidden="true"><path d="M3.5 1.5l2.5 2.8-1.3 1.9c.9 2 2.4 3.5 4.4 4.4l1.9-1.3 2.8 2.5-1.4 2.4C7 13.5 2.5 9 1.3 3l2.2-1.5z" fill="#fff"/></svg>
        <span class="contact-text">+351 214507781 | 214507781)</span>
      </li>
      <li class="contact-item contact-item--email">
        <svg viewBox="0 0 16 16" aria-hidden="true"><rect x="1.5" y="3.5" width="13" height="9" fill="none" stroke="#fff" stroke-width="1.4"/><path d="M1.5 3.5l6.5 5 6.5-5" fill="none" stroke="#fff" stroke-width="1.4"/></svg>
        <span class="contact-text">veltrano.oficina@mail.pt</span>
      </li>
      <li class="contact-item contact-item--web">
        <svg viewBox="0 0 16 16" aria-hidden="true"><rect x="1.5" y="1.5" width="13" height="13" rx="2" fill="#fff"/></svg>
        <span class="contact-text">www.veltrano-oficina.pt</span>
      </li>
    </ul>
  </section>

  <h1 class="view-label view-label--back">Back View</h1>

  <section class="card card--back">
    <div class="metal-panel" role="img" aria-label="Dark perforated metal texture background"></div>

    <svg class="stripe-top" viewBox="0 0 660 15" aria-hidden="true">
      <rect x="0" y="0" width="660" height="15" fill="#ffffff"/>
      <polygon points="416,0 424,0 416,15 408,15" fill="#2e779e"/>
      <polygon points="496,0 504,0 496,15 488,15" fill="#2e779e"/>
      <polygon points="578,0 586,0 578,15 570,15" fill="#2e779e"/>
    </svg>

    <h2 class="services-title">OUR SERVICES</h2>
    <ul class="services-list">
      <li class="service">Serviço mecânico</li>
      <li class="service">Peritagem</li>
      <li class="service">Serviço pintura</li>
      <li class="service">Orçamento</li>
      <li class="service">Revisão</li>
    </ul>

    <div class="wordmark">VELTRANO</div>
    <div class="person-name">RUI MATOS</div>
    <div class="person-role">Managing Director<br>+351 910482736</div>

    <div class="stripe-bottom">https:www//yourdomain.com</div>
  </section>
</div>
</body>
</html>
```